PowerPoint design MedoraVix

We need a PowerPoint set-up based upon our existing logo (see joint file)
Our company is operating in the health care and life science sector. We are mainly focussing on international business

Target Market(s)

International

Industry/Entity Type

health care and life sciences

Requirements
Must have
• Logos as added

```html
<!DOCTYPE html>
<html lang="en">
<head>
<meta charset="utf-8">
<title>Section Divider</title>
<link rel="stylesheet" href="https://fonts.googleapis.com/css2?family=Carlito:wght@400;700&display=swap">
<style>
  :root {
    --navy: #0b4a80;
    --green: #5cbf14;
    --navy-soft: rgba(11, 74, 128, 0.16);
    --green-soft: rgba(92, 191, 20, 0.16);
    --ink: #404040;
    --paper: #ffffff;
  }
  html, body {
    margin: 0;
    padding: 0;
    width: 1200px;
    height: 675px;
    overflow: hidden;
    background: var(--paper);
  }
  .slide {
    position: relative;
    width: 1200px;
    height: 675px;
    background: var(--paper);
    font-family: "Carlito", "Calibri", sans-serif;
    font-variant-ligatures: no-common-ligatures;
  }
  .wave-band {
    position: absolute;
    left: 0;
    top: 180px;
    width: 420px;
    height: 116px;
    background: linear-gradient(90deg, var(--navy-soft) 0%, var(--green-soft) 50%, var(--navy-soft) 100%);
    border-radius: 0 58px 58px 0;
  }
  .section-number {
    position: absolute;
    left: 416px;
    top: 257px;
    width: 57px;
    height: 57px;
    border-radius: 50%;
    background: var(--navy);
    color: var(--paper);
    font-weight: 700;
    font-size: 22px;
    display: flex;
    align-items: center;
    justify-content: center;
  }
  .section-title {
    position: absolute;
    left: 498px;
    top: 266px;
    margin: 0;
    font-size: 33px;
    font-weight: 700;
    color: var(--navy);
    line-height: 40px;
    white-space: nowrap;
  }
  .section-subtitle {
    position: absolute;
    left: 498px;
    top: 346px;
    margin: 0;
    font-size: 19px;
    font-weight: 400;
    color: var(--ink);
    line-height: 24px;
    white-space: nowrap;
  }
</style>
</head>
<body>
  <main class="slide">
    <div class="wave-band" role="img" aria-label="Decorative flowing wave lines in navy and green leading to the section number"></div>
    <div class="section-number">1</div>
    <h1 class="section-title">Section Divider Sample</h1>
    <p class="section-subtitle">Sub-Section Divider Sample</p>
  </main>
</body>
</html>
```